Business Card

I need a business card for my work as an energy lawyer. I am a single prctioner and I consult to energy companies regarding a variety of legal issues involving environmental matters, energy efficiency, regulations and contractual arrangements. i need a distinctive business card that stands out and is easy to read. I like bold colors or high contrast. I like a sparse architectural design. The font should be easy to read (many of my clients use reading glasses and are concerned about small type). The card should communicate that I am somewhat different from ordinary legal counsel. Below are some examples of cards that I like. Thank you for your interest and thought. Glenn Dusty Harker
Updates

Thanks to everyone who has submitted a design.  My general comments are:

1.  I like the colourful cards and the high contrast cards.
2.  I prefer the use of icons for home address, phone, mobile and email.
3.  For the high contrast cards please use three colours - black background, and red and white for the logo or information.
4.  The mobile number area code should be 403 and not 404.
5.  I also need to add a direct phone line which is 403-517-6392.

Thank you,

Glenn Harker

Reason: I have briefly extended the deadline by three days to allow those individuals who responded early to revise their designs based upon the subsequent clarification of the colours (red, white, black background) and the request to use icons and add a direct phone number.

Industry/Entity Type

Business

```html
<!DOCTYPE html>
<html lang="en">
<head>
<meta charset="utf-8">
<title>Glenn Dusty Harker – Business Card</title>
<link href="https://fonts.googleapis.com/css2?family=Delius&display=swap" rel="stylesheet">
<style>
  :root {
    --ink: #0a0a0a;
    --paper: #ffffff;
    --accent: #e11b22;
    --divider: #9a9a9a;
    --backdrop: #e7e4e0;
    --card-w: 520px;
    --card-h: 297px;
  }
  * { box-sizing: border-box; margin: 0; padding: 0; }
  html, body { width: 1200px; height: 811px; overflow: hidden; }
  body {
    background: var(--backdrop);
    font-family: "Delius", "Comic Neue", sans-serif;
    position: relative;
  }
  .card {
    position: absolute;
    width: var(--card-w);
    height: var(--card-h);
    overflow: hidden;
    box-shadow: 0 6px 18px rgba(0,0,0,.25);
  }
  .card--front { left: 60px; top: 70px; background: var(--paper); }
  .card--back { left: 620px; top: 440px; background: var(--ink); }

  .card__swoosh { position: absolute; inset: 0; }

  .brand-name {
    color: var(--accent);
    font-size: 22px;
    letter-spacing: .3px;
    white-space: nowrap;
  }
  .front__brand {
    position: absolute; left: 22px; top: 62px; width: 256px;
    display: flex; align-items: center; gap: 8px;
  }
  .brand-dot { width: 9px; height: 9px; border-radius: 50%; background: var(--accent); flex: none; }

  .front__divider {
    position: absolute; left: 292px; top: 18px; width: 1px; height: 60px;
    background: var(--divider);
  }
  .front__identity { position: absolute; left: 300px; top: 24px; width: 210px; text-align: center; }
  .identity__name { color: var(--ink); font-size: 19px; white-space: nowrap; }
  .identity__title { color: var(--accent); font-size: 11.5px; line-height: 1.45; margin-top: 6px; }

  .contact-list {
    position: absolute; left: 250px; top: 150px; list-style: none;
    color: var(--paper); font-size: 12px;
  }
  .contact-list__item { display: flex; align-items: flex-start; gap: 18px; margin-bottom: 12px; line-height: 1.5; }
  .contact-list__icon { width: 12px; height: 12px; margin-top: 3px; flex: none; fill: var(--paper); }

  .web-address { color: var(--paper); font-size: 10.5px; letter-spacing: .4px; white-space: nowrap; }
  .front__web { position: absolute; left: 80px; top: 262px; }

  .back__band {
    position: absolute; left: 0; right: 0; top: 112px; height: 98px;
    background: var(--paper);
    display: flex; align-items: center; justify-content: center; gap: 10px;
  }
  .back__band .brand-name { font-size: 28px; }
  .back__web { position: absolute; left: 0; right: 0; top: 224px; text-align: center; }
</style>
</head>
<body>

  <section class="card card--front" aria-label="Business card front">
    <svg class="card__swoosh" viewBox="0 0 520 297" aria-hidden="true">
      <path d="M0,297 L0,196 Q230,108 520,88 L520,297 Z" fill="var(--ink)"/>
      <path d="M0,214 Q215,126 520,98 Q230,146 0,240 Z" fill="var(--paper)"/>
    </svg>

    <div class="front__brand">
      <span class="brand-dot"></span>
      <span class="brand-name">Glenn Dusty Harker</span>
    </div>

    <div class="front__divider"></div>

    <div class="front__identity">
      <p class="identity__name">Glenn Dusty Harker</p>
      <p class="identity__title">Barrister and Solicitor,<br>LLB, ICD.D</p>
    </div>

    <ul class="contact-list">
      <li class="contact-list__item">
        <svg class="contact-list__icon" viewBox="0 0 12 12" aria-label="Address"><path d="M6 0a4 4 0 0 0-4 4c0 3 4 8 4 8s4-5 4-8a4 4 0 0 0-4-4zm0 5.6A1.6 1.6 0 1 1 6 2.4a1.6 1.6 0 0 1 0 3.2z"/></svg>
        <span>2740 Kestrel Avenue S.W.,<br>Calgary, Alberta</span>
      </li>
      <li class="contact-list__item">
        <svg class="contact-list__icon" viewBox="0 0 12 12" aria-label="Mobile"><path d="M3 0h6a1 1 0 0 1 1 1v10a1 1 0 0 1-1 1H3a1 1 0 0 1-1-1V1a1 1 0 0 1 1-1zm.5 1.5v8h5v-8zM6 10.2a.6.6 0 1 0 0 1.2.6.6 0 0 0 0-1.2z"/></svg>
        <span>1.403.555.0147</span>
      </li>
      <li class="contact-list__item">
        <svg class="contact-list__icon" viewBox="0 0 12 12" aria-label="Direct line"><path d="M2.6 0.4l1.8 2.3c.3.4.2.9-.1 1.2l-.8.8c.6 1.4 1.9 2.7 3.3 3.3l.8-.8c.3-.3.8-.4 1.2-.1l2.3 1.8c.4.3.4.9.1 1.300l-1 1c-.6.6-1.5.8-2.3.5C4.6 10.5 1.5 7.4.3 4.1 0 3.3.2 2.4.8 1.8l1-1c.3-.4.5-.6.8-.4z"/></svg>
        <span>403-517-6392</span>
      </li>
      <li class="contact-list__item">
        <svg class="contact-list__icon" viewBox="0 0 12 12" aria-label="Email"><path d="M0 2.5h12v7H0zm1 .8v.3L6 6.8l5-3.2v-.3zm0 1.4V8.7h10V4.7L6 7.9z"/></svg>
        <span>dusty@dustyharker.com</span>
      </li>
    </ul>

    <p class="web-address front__web">www.dustyharker.com</p>
  </section>

  <section class="card card--back" aria-label="Business card back">
    <div class="back__band">
      <span class="brand-dot"></span>
      <span class="brand-name">Glenn Dusty Harker</span>
    </div>
    <p class="web-address back__web">www.dustyharker.com</p>
  </section>

</body>
</html>
```